Trifold Brochure needed for Elm Path Counseling

Hi! We need to have a trifold brochure made.

We would like to see brochure designs that use our logo colors, which are khaki, chocolate brown, and gray.

The brochure should be a modern design and please use your creativity.

Brochure is a trifold brochure, size is 8.5 x 11 and full color.

The following attachment has the content to be used in the trifold brochure, as well as some possible pictures. I have also attached our logo.

We would like to use file #2 for sure (picture number 27193540) and add the quote from her...

"At first, I was reluctant about going to ElmPath. Once I got there, I was glad I went. I learned a lot and was treated like family the whole time." Maren Colby

Requirements
Must have
• Our logo
• Information should be listed exactly as the attached document
• You must stick with our logo colors

```html
<!DOCTYPE html>
<html lang="en">
<head>
<meta charset="utf-8">
<title>Elm Path Counseling – Trifold Brochure</title>
<link rel="stylesheet" href="https://fonts.googleapis.com/css2?family=Cinzel:wght@400;700&family=Ubuntu:wght@400;500;700&family=Ubuntu+Condensed&display=swap">
<style>
  :root {
    --chocolate: #6b3a14;
    --brown: #7a4317;
    --amber: #c0701c;
    --khaki: #b89a6a;
    --gray: #8d8d8f;
    --ink: #1e1e1e;
    --paper: #ffffff;
  }
  * { margin: 0; padding: 0; box-sizing: border-box; }
  html, body { width: 1200px; height: 933px; overflow: hidden; background: var(--paper); }
  .brochure { position: relative; width: 1200px; height: 933px; overflow: hidden; font-family: "Ubuntu", sans-serif; color: var(--ink); }
  .backdrop { position: absolute; inset: 0; }
  .panel-text { position: absolute; top: 206px; }
  .faq { left: 38px; width: 340px; }
  .reminders { left: 421px; width: 356px; }
  .section-title { font-weight: 700; font-size: 16.5px; line-height: 22px; letter-spacing: -0.2px; color: var(--chocolate); margin-bottom: 11px; }
  .faq-question { font-weight: 700; font-size: 15px; line-height: 20px; color: var(--chocolate); margin-bottom: 11px; }
  .faq-answer { font-family: "Ubuntu Condensed", sans-serif; font-size: 16px; line-height: 19.5px; text-align: justify; margin-bottom: 11px; }
  .faq-answer.plain { text-align: left; }
  .faq-answer small { display: block; font-size: 11px; line-height: 13px; text-align: left; }
  .reminder-strong { font-weight: 700; font-size: 15px; line-height: 20px; margin-bottom: 11px; }
  .reminder-body { font-family: "Ubuntu Condensed", sans-serif; font-size: 16px; line-height: 19.5px; margin-bottom: 11px; }
  .reminder-body b { font-family: "Ubuntu", sans-serif; font-size: 15px; font-weight: 700; }
  .closing { font-weight: 700; font-size: 15px; line-height: 20px; letter-spacing: -0.3px; color: var(--chocolate); margin-bottom: 26px; }
  .contact-line { display: flex; align-items: center; gap: 9px; color: var(--chocolate); font-weight: 700; }
  .contact-phone { font-size: 35px; line-height: 36px; }
  .contact-email { font-size: 20px; line-height: 26px; }
  .contact-line svg { flex: none; }
  .brand { position: absolute; left: 868px; top: 50px; display: flex; align-items: center; gap: 14px; }
  .brand-mark { width: 48px; height: 48px; border-radius: 50%; background: var(--gray); }
  .brand-name { font-weight: 500; color: var(--brown); text-align: right; }
  .brand-name .word { display: block; font-size: 38px; line-height: 40px; }
  .brand-name .sub { display: block; font-size: 13px; line-height: 16px; letter-spacing: 4.5px; }
  .brand-tag { position: absolute; left: 884px; top: 127px; font-size: 12px; color: var(--gray); letter-spacing: 0.7px; }
  .motto { position: absolute; right: 52px; top: 697px; text-align: right; font-family: "Cinzel", serif; color: var(--chocolate); }
  .motto-line1 { font-size: 25px; line-height: 28px; letter-spacing: 1px; }
  .motto-line2 { font-size: 25px; line-height: 50px; letter-spacing: 1px; margin-right: 44px; }
  .motto-line2 .big { font-size: 48px; font-weight: 700; }
  .motto-line3 { font-size: 25px; line-height: 26px; letter-spacing: 1px; }
</style>
</head>
<body>
<main class="brochure">
  <svg class="backdrop" width="1200" height="933" viewBox="0 0 1200 933" xmlns="http://www.w3.org/2000/svg">
    <defs>
      <linearGradient id="paperFade" x1="0" y1="0" x2="1" y2="0">
        <stop offset="0" stop-color="#ffffff"/>
        <stop offset="1" stop-color="#e2e2e3"/>
      </linearGradient>
      <linearGradient id="quoteFade" x1="0" y1="0" x2="0" y2="1">
        <stop offset="0" stop-color="#ffffff"/>
        <stop offset="1" stop-color="#d3d3d5"/>
      </linearGradient>
      <linearGradient id="topPhotoTone" x1="0" y1="0" x2="1" y2="0">
        <stop offset="0" stop-color="#d9b7a0"/>
        <stop offset="0.5" stop-color="#e6dccd"/>
        <stop offset="1" stop-color="#c9a48c"/>
      </linearGradient>
      <linearGradient id="parkPhotoTone" x1="0" y1="0" x2="0" y2="1">
        <stop offset="0" stop-color="#a9b86a"/>
        <stop offset="0.3" stop-color="#c4b08a"/>
        <stop offset="0.6" stop-color="#d9a59a"/>
        <stop offset="1" stop-color="#4e6a8e"/>
      </linearGradient>
      <linearGradient id="handsPhotoTone" x1="0" y1="0" x2="1" y2="1">
        <stop offset="0" stop-color="#c9a06a"/>
        <stop offset="0.5" stop-color="#8a5f45"/>
        <stop offset="1" stop-color="#3f5a5a"/>
      </linearGradient>
    </defs>

    <rect x="0" y="0" width="400" height="933" fill="url(#paperFade)"/>
    <rect x="400" y="0" width="395" height="933" fill="#ffffff"/>
    <rect x="795" y="0" width="405" height="933" fill="url(#quoteFade)"/>

    <path role="img" aria-label="Photo of smiling seniors giving a thumbs up" d="M0 0 H795 V0 C700 60 520 150 380 168 C250 183 100 185 0 176 Z" fill="url(#topPhotoTone)"/>
    <path d="M0 176 C100 185 250 183 380 168 C520 150 700 60 795 0 L795 6 C700 72 520 160 380 178 C250 192 100 192 0 184 Z" fill="var(--chocolate)"/>

    <path role="img" aria-label="Photo of a laughing senior couple with a bicycle in a park" d="M795 150 C900 175 1050 190 1200 178 V614 C1100 616 950 622 795 636 Z" fill="url(#parkPhotoTone)"/>
    <path d="M795 140 C900 168 1050 182 1200 170 V178 C1050 190 900 175 795 150 Z" fill="var(--chocolate)"/>
    <path d="M700 85 C760 120 790 135 795 140" fill="none" stroke="var(--amber)" stroke-width="1.2"/>

    <path role="img" aria-label="Photo of two people holding hands" d="M400 790 C520 720 660 665 795 642 V933 H400 Z" fill="url(#handsPhotoTone)"/>

    <path role="img" aria-label="Photo of a smiling senior woman resting her chin on her hand" d="M230 933 C290 880 340 835 400 800 V933 Z" fill="var(--khaki)" fill-opacity="0.55"/>

    <path d="M120 933 C250 850 420 760 600 690 C720 645 820 628 1000 620 C1090 616 1150 615 1200 614 V622 C1150 622 1090 624 1000 628 C830 636 720 656 600 700 C420 770 260 862 150 933 Z" fill="var(--amber)"/>
    <path d="M795 636 C950 622 1100 616 1200 614 V608 C1100 610 950 614 795 628 Z" fill="var(--chocolate)"/>

    <line x1="400" y1="0" x2="400" y2="933" stroke="#cfcfcf" stroke-width="1"/>
    <line x1="795" y1="0" x2="795" y2="933" stroke="#cfcfcf" stroke-width="1"/>
  </svg>

  <section class="panel-text faq">
    <h2 class="section-title">FREQUENTLY ASKED QUESTIONS</h2>
    <h3 class="faq-question">What can I expect at my appointment?</h3>
    <p class="faq-answer">You can Expect to be treated like family through&shy;out the entire visit. We will Respect your time and are dedicated to helping you better understand proactive opioid education.</p>
    <h3 class="faq-question">How long will my appointment last?</h3>
    <p class="faq-answer">Please allow 45 minutes to complete your visit.<small>(this allows time to complete your paperwork)</small></p>
    <h3 class="faq-question">Will my information be kept confidential?</h3>
    <p class="faq-answer">Yes, your visit will only be shared with your referring doctor. ElmPath Counseling is HIPAA Compliant.</p>
    <h3 class="faq-question">Why do you need my ID and Insurance Card?</h3>
    <p class="faq-answer">Your ID and insurance card are needed for verifica&shy;tion and any labs tests that may be requested.</p>
    <h3 class="faq-question">How much is my visit?</h3>
    <p class="faq-answer plain">The office visit is only $40.<small>(we have a hardship program for those in need)</small></p>
    <h3 class="faq-question">Is this visit a one time appointment?</h3>
    <p class="faq-answer plain">ElmPath sees patients 3 to 4 times a year Providing New Educational material and tools each time.<small>(too much information for 1 visit )</small></p>
  </section>

  <section class="panel-text reminders">
    <h2 class="section-title">APPOINTMENT REMINDERS</h2>
    <p class="reminder-strong">Please bring Picture ID and Insurance Card (s)</p>
    <p class="reminder-strong">Please allow us up to 45 mins of your time to give you the best possible experience.</p>
    <p class="reminder-body"><b>Our office visit is only $40.</b><br>We accept credit, your check or cash.</p>
    <p class="reminder-body"><b>We are anxious to see You!</b><br>Please do not miss your appointment, a 25.00 no show fee will be applied.</p>
    <p class="reminder-body">ElmPath is a stepping stone for Future Success, and Your Future Success should be determined by how much You impact Your community.</p>
    <p class="closing">Therefore, let's work Together in Making Solutions, One Patient at a time.</p>
    <p class="contact-line contact-phone">
      <svg width="28" height="24" viewBox="0 0 28 24" aria-hidden="true"><path d="M2 8 C2 2 26 2 26 8 L22 10 L19 6 H9 L6 10 Z" fill="var(--chocolate)"/><rect x="5" y="11" width="18" height="11" rx="2" fill="var(--chocolate)"/><circle cx="14" cy="16.5" r="3" fill="#fff"/></svg>
      404.555.0182
    </p>
    <p class="contact-line contact-email">
      <svg width="24" height="24" viewBox="0 0 22 22" aria-hidden="true"><circle cx="11" cy="11" r="10" fill="var(--chocolate)"/><path d="M6 6 C9 7 9 10 7 12 C9 14 10 16 9 19 M14 4 C13 7 16 8 18 8 M13 13 C15 12 17 14 17 17" fill="none" stroke="#fff" stroke-width="1.6"/></svg>
      info@elmpathcounseling.com
    </p>
  </section>

  <div class="brand">
    <span class="brand-mark"></span>
    <span class="brand-name"><span class="word">ElmPath</span><span class="sub">COUNSELING</span></span>
  </div>
  <p class="brand-tag">a pro-active opioid education center</p>

  <blockquote class="motto">
    <div class="motto-line1">“Making Solutions</div>
    <div class="motto-line2"><span class="big">ONE</span> Patient</div>
    <div class="motto-line3">at a time”</div>
  </blockquote>
</main>
</body>
</html>
```